Financial Workshop for Halvorsen Financial

Postcard to comply with PRLQ. Invitation to workshop for 55+ senior community.
"Estate Conservation Strategies and Legacy Planning"
Building a sound and lasting retirement portfolio with a focus on growth and asset protection.
Developing investment objectives
Understanding risk adversity
Preserving assets
Conservative growth strategies for saving and investing
Planning for uncovered health care costs
Estate planning
Reid Halvorsen, Certified Financial Plannerâ„¢

add to the text (bullets) after Estate Planning (on same line) and Wealth Transfer Strategies Thank you Added Friday, October 13, 2017

Target Market(s)

Seniors

Industry/Entity Type

Financial

Font styles to use
Sans Serif

Colors

Designer to choose colors to be used in the design.

Requirements
Must have
• Logo
• Eye-catching images
• Easy to read geared for seniors
• Upscale professional look
• Afresh new look from previous samples sent.
Nice to have
• Something that stands out among the many postcard mail pieces they will get.
Should not have
• aside from logo/photo samples are an example of previous workshops and should not be reused.

```html
<!DOCTYPE html>
<html lang="en">
<head>
<meta charset="utf-8">
<title>Halvorsen Financial – Estate Conservation Workshop Mailer</title>
<link href="https://fonts.googleapis.com/css2?family=Source+Sans+3:wght@300;400;600;700&display=swap" rel="stylesheet">
<style>
  :root{
    --stage:#fdf0cf;
    --navy:#2e2a7a;
    --navy-text:#2b2d83;
    --wave:#7b76c4;
    --white:#ffffff;
    --gear:#c9c9cb;
    --orange-a:#f58a1f; --orange-b:#ef4d2e;
    --lime-a:#d7e02c; --lime-b:#b8cf3a;
    --rose-a:#e8707a; --rose-b:#d9475c;
    --teal-a:#4bb7cf; --teal-b:#3498ad;
    --stone-a:#e8e4df; --stone-b:#d6d0c8;
    --sand-a:#e3d5b8; --sand-b:#cdb994;
    --leaf-a:#93cc6e; --leaf-b:#6cae4a;
    --plum-a:#b870b4; --plum-b:#9a4f9c;
    --body:"Source Sans 3", Arial, sans-serif;
  }
  *{box-sizing:border-box;margin:0;padding:0}
  html,body{width:1200px;height:960px;overflow:hidden}
  body{background:var(--stage);font-family:var(--body);position:relative;color:var(--navy-text)}

  .card{position:absolute;background:var(--white);box-shadow:3px 4px 6px rgba(0,0,0,.18);overflow:hidden}
  .card--front{left:28px;top:101px;width:512px;height:739px}
  .card--back{left:562px;top:260px;width:608px;height:422px}

  .photo{position:absolute;background:linear-gradient(135deg,#f3f1ec 0%,#d9d2c4 45%,#a89a86 75%,#e7e1d6 100%)}
  .card--front .photo{left:0;top:0;width:512px;height:345px}
  .card--back .photo{left:0;top:0;width:420px;height:280px}

  .brand{position:absolute;background:var(--white);display:flex;align-items:center}
  .brand__name{font-weight:600;color:var(--navy);line-height:1;letter-spacing:.5px;white-space:nowrap}
  .card--front .brand{left:0;top:37px;width:272px;height:72px;padding-left:36px}
  .card--front .brand__name{font-size:24px}
  .card--back .brand{left:0;top:36px;width:208px;height:56px;padding-left:20px}
  .card--back .brand__name{font-size:18px}

  .front-title{position:absolute;left:42px;top:360px;font-weight:700;font-size:23.5px;line-height:27px;color:var(--navy-text);white-space:nowrap}
  .front-presenter{position:absolute;left:42px;top:415px;font-weight:700;font-size:13px;line-height:16px;letter-spacing:-.2px;color:var(--navy-text);white-space:nowrap}
  .front-presenter sup{font-size:8px}
  .presenter-photo{position:absolute;left:338px;top:389px;width:48px;height:68px;background:linear-gradient(#8c95a6,#4a5063);border:1px solid #777;z-index:2}
  .date-band{position:absolute;left:0;top:438px;width:512px;height:22px;background:var(--navy);color:var(--white);font-size:14px;line-height:22px;padding-left:44px}
  .front-lede{position:absolute;left:42px;top:468px;width:440px;font-size:14px;line-height:19px;color:var(--navy-text)}

  .gear{position:absolute;background:var(--gear)}
  .gear--left{left:13px;top:547px;width:143px;height:132px;border-radius:50%}
  .gear--right{left:420px;top:506px;width:44px;height:60px;border-radius:50%}

  .topic{position:absolute;display:flex;align-items:center;justify-content:center;text-align:center;color:var(--white);font-size:14.5px;line-height:19px;font-weight:400;border:1px solid rgba(0,0,0,.25)}
  .topic--objectives{left:80px;top:513px;width:170px;height:72px;background:linear-gradient(var(--orange-a) 40%,var(--orange-b) 40%)}
  .topic--healthcare{left:255px;top:503px;width:169px;height:68px;background:linear-gradient(var(--lime-a) 50%,var(--lime-b) 50%);color:#3e3f8a}
  .topic--strategies{left:53px;top:593px;width:103px;height:42px;background:linear-gradient(var(--rose-a) 50%,var(--rose-b) 50%)}
  .topic--growth{left:274px;top:569px;width:184px;height:90px;background:linear-gradient(var(--stone-a) 55%,var(--stone-b) 55%);color:#5a3f7e}
  .topic--risk{left:154px;top:581px;width:130px;height:70px;background:linear-gradient(var(--teal-a) 50%,var(--teal-b) 50%)}
  .topic--estate{left:81px;top:645px;width:129px;height:44px;background:linear-gradient(var(--sand-a) 50%,var(--sand-b) 50%);color:#4a4a6a}
  .topic--wealth{left:182px;top:657px;width:130px;height:44px;background:linear-gradient(var(--leaf-a) 50%,var(--leaf-b) 50%);color:#3d3f80}
  .topic--preserving{left:318px;top:651px;width:132px;height:44px;background:linear-gradient(var(--plum-a) 50%,var(--plum-b) 50%)}

  .back-wave{position:absolute;left:0;top:0;width:608px;height:422px}
  .back-intro{position:absolute;left:441px;top:50px;width:150px;font-size:8.8px;line-height:11.2px;color:var(--navy-text)}
  .back-topics{position:absolute;left:441px;top:96px;width:146px;list-style:none;font-size:8.8px;line-height:11.2px;color:var(--navy-text)}
  .back-topics li{padding-left:8px;position:relative}
  .back-topics li::before{content:"•";position:absolute;left:0}
  .back-title{position:absolute;left:15px;top:237px;width:200px;text-align:center;font-weight:700;font-size:11px;line-height:14px;color:var(--navy-text)}
  .event-details{position:absolute;left:47px;top:278px;font-size:8.5px;line-height:11px;color:var(--navy-text);display:grid;grid-template-columns:41px auto}
  .food-band{position:absolute;left:0;top:317px;width:294px;height:36px;background:var(--navy);border-radius:0 18px 18px 0;color:var(--white);font-weight:600;font-size:8.5px;line-height:11px;padding:7px 0 0 24px}
  .food-band__icon{position:absolute;right:16px;top:5px}
  .contact{position:absolute;left:34px;top:364px;font-style:normal;font-weight:600;font-size:8.5px;line-height:11px;color:var(--navy-text)}
  .mail-address{position:absolute;left:328px;top:312px;width:168px;height:48px;border:1.5px solid #222;font-family:Arial, sans-serif;font-size:10.5px;line-height:13px;color:#111;padding:10px 0 0 7px}
  .indicia{position:absolute;left:514px;top:288px;width:72px;height:72px;border:1.2px dashed #222;font-family:Arial, sans-serif;font-size:8.5px;line-height:11px;text-align:center;color:#111;padding-top:5px}
</style>
</head>
<body>

<section class="card card--front" aria-label="Workshop flyer">
  <div class="photo" role="img" aria-label="Photo of a smiling senior couple at a café table looking at a tablet"></div>
  <div class="brand"><span class="brand__name">Halvorsen Financial</span></div>

  <h1 class="front-title">Estate Conservation Strategies<br>and Legacy Planning</h1>
  <p class="front-presenter">Reid Halvorsen, Certified Financial Planner<sup>™</sup></p>
  <div class="presenter-photo" role="img" aria-label="Portrait photo of the presenter"></div>
  <div class="date-band">November 7th at 6:30 PM @ Linden Hall</div>
  <p class="front-lede">Building a sound and lasting retirement portfolio with a focus on growth and income</p>

  <div class="gear gear--left" role="img" aria-label="Grey gear decoration"></div>
  <div class="gear gear--right" role="img" aria-label="Grey gear decoration"></div>

  <div class="topic topic--objectives">Developing<br>Investment Objectives</div>
  <div class="topic topic--healthcare">Planning for Uncovered<br>Healthcare Costs</div>
  <div class="topic topic--strategies">Strategies</div>
  <div class="topic topic--growth">Conservative Growth<br>Strategies for<br>Saving and Investing</div>
  <div class="topic topic--risk">Understanding<br>Risk Adversity</div>
  <div class="topic topic--wealth">Wealth<br>Transfer</div>
  <div class="topic topic--estate">Estate Planning</div>
  <div class="topic topic--preserving">Preserving Assets</div>
</section>

<section class="card card--back" aria-label="Mailing postcard">
  <div class="photo" role="img" aria-label="Photo of a smiling senior couple at a café table looking at a tablet"></div>
  <svg class="back-wave" viewBox="0 0 608 422" aria-hidden="true">
    <path d="M0,254 C60,215 120,202 200,225 C290,252 350,282 420,276 C510,268 570,225 608,176 L608,422 L0,422 Z" fill="#ffffff"/>
    <path d="M0,254 C60,215 120,202 200,225 C290,252 350,282 420,276 C510,268 570,225 608,176" fill="none" stroke="var(--wave)" stroke-width="6"/>
  </svg>
  <div class="brand"><span class="brand__name">Halvorsen Financial</span></div>

  <p class="back-intro">Building a sound and lasting retirement portfolio with a focus on growth and income</p>
  <ul class="back-topics">
    <li>Developing Investment Objectives</li>
    <li>Understanding Risk Adversity</li>
    <li>Preserving Assets</li>
    <li>Conservative Growth Strategies for Saving and Investing</li>
    <li>Planning for Uncovered Healthcare Costs</li>
    <li>Estate Planning</li>
    <li>Wealth Transfer</li>
    <li>Strategies</li>
  </ul>

  <h2 class="back-title">Estate Conservation<br>Strategies and Legacy Planning</h2>
  <div class="event-details">
    <span>When:</span><span>November 7th at 6:30 PM</span>
    <span>Where:</span><span>Linden Hall</span>
  </div>

  <div class="food-band">Gourmet Deli Sandwiches, Fresh fruit, Cheese cake and<br>Refreshments will be provided
    <svg class="food-band__icon" width="34" height="26" viewBox="0 0 34 26" aria-hidden="true">
      <path d="M19 6 H31 L29 25 H21 Z" fill="#fff"/>
      <path d="M27 6 L30 0" stroke="#fff" stroke-width="1.5"/>
      <rect x="1" y="13" width="15" height="3" rx="1.5" fill="#fff"/>
      <rect x="1" y="18" width="15" height="3" rx="1.5" fill="#fff"/>
      <rect x="1" y="23" width="15" height="3" rx="1.5" fill="#fff"/>
    </svg>
  </div>

  <address class="contact">418 Maple Crest Lane, Raleigh, NC 27603<br>Phone: 919-555-0148</address>

  <div class="mail-address">Local<br>Postal Customer</div>
  <div class="indicia">PRSRT STD<br>ECRWSS<br>U.S. POSTAGE<br>PAID<br>PRLQ RETAIL</div>
</section>

</body>
</html>
```